Corporate marketing website with signup form

The function of the website is to promote our 2 product offerings. It will contain a main screen and several 5-7 sub-pages that will be available as 'scroll down' anchors and as front-page navigation links on the top of the page.

Navigation menu labels are: Products, Unique Model, Pricing, About, and Contact

Target Market(s)

Business to business marketers who are looking to source lead generation services

Industry/Entity Type

Marketing

Logo Text

Velmora

Coding

Coded - Design and coding required

Number of Pages Required

5+ page

Requirements
Must have
• A sign-up form on main section of the front page. Fields are First Name, Last Name, Company, and Email (all text), and a pull-down with three options (only pick one): Track 1, Track 2, Custom Combination.
• Also incorporate the bottom half (ie crop the image) of the EPS file attached (the 'blue heads). Add this to the lower portion of the main screen and have the rest of the blue background become the background for the next anchored section of the navigation.
• You'll see the main section text in the mock-up I provided. The rest of the menu items/anchors can be lorem ipsum for now.
• Can this be coded in Wordpress? That would be my preference so I can edit it in the future.

```html
<!DOCTYPE html>
<html lang="en">
<head>
<meta charset="utf-8">
<title>Velmora – List and Audience Building</title>
<link href="https://fonts.googleapis.com/css2?family=Bree+Serif&family=Montserrat:wght@400;700&family=Lato:wght@400;700&display=swap" rel="stylesheet">
<style>
:root{
  --navy:#1b2330;
  --navy-deep:#141a24;
  --blue:#1fa3e0;
  --blue-dark:#1586c2;
  --sky:#c9d6e0;
  --paper:#efefef;
  --white:#ffffff;
  --ink:#222222;
  --muted:#555555;
  --orange:#f08a24;
  --teal:#2a8fc9;
  --green:#4aa33c;
  --field:#2a3442;
}
*{box-sizing:border-box;margin:0;padding:0}
html,body{width:1200px;height:3199px;overflow:hidden}
body{font-family:"Lato",Arial,sans-serif;color:var(--ink);background:var(--white);position:relative}
section,header{position:absolute;left:0;width:1200px}
.abs{position:absolute}

/* header */
.topbar{top:0;height:86px;background:var(--navy)}
.brand{left:86px;top:22px;display:flex;align-items:center;gap:12px}
.brand-mark{width:30px;height:30px;background:var(--blue)}
.brand-name{font-family:"Montserrat",sans-serif;font-size:36px;color:var(--white);letter-spacing:1px}
.contact-chip{top:22px;display:flex;align-items:center;gap:14px;color:var(--white)}
.contact-chip small{display:block;font-size:11px;letter-spacing:1px;opacity:.8}
.contact-chip strong{font-family:"Montserrat",sans-serif;font-size:19px}
.chip-phone{left:587px}
.chip-mail{left:872px}

.hero{top:86px;height:684px;background:linear-gradient(180deg,#d6e1ea 0%,#b8c8d4 55%,#8aa0b0 100%)}
.mainnav{left:194px;top:0;width:831px;height:46px;background:var(--blue);display:flex;justify-content:space-around;align-items:center;border-bottom:2px solid var(--blue-dark)}
.mainnav a{color:var(--white);text-decoration:none;font-family:"Montserrat",sans-serif;font-size:14px;font-weight:700;text-transform:uppercase}
.hero-title{top:86px;width:1200px;text-align:center;font-family:"Bree Serif",serif;font-size:35px;color:var(--ink)}
.hero-sub{top:146px;width:1200px;text-align:center;font-family:"Montserrat",sans-serif;font-weight:700;font-size:23px;color:var(--ink)}
.track{top:251px;height:328px;background:var(--blue);border-radius:26px;padding:16px;box-shadow:0 20px 24px rgba(0,0,0,.35)}
.track-inner{background:var(--white);border-radius:18px;height:100%;padding:12px 16px;text-align:center;overflow:hidden}
.track h3{font-family:"Lato",sans-serif;font-weight:400;font-size:31px;margin-bottom:8px}
.track p{font-size:14px;font-weight:700;line-height:1.45;color:var(--ink)}
.track-1{left:61px;width:349px}
.track-2{left:430px;width:351px}
.track-2 p{margin-top:36px}
.track-pointer{top:454px;width:0;height:0;border-top:18px solid transparent;border-bottom:18px solid transparent;border-left:16px solid var(--white)}
.track-form{left:797px;width:348px}
.track-form h3{font-size:28px;font-weight:700;margin-bottom:0;line-height:1}
.track-form h4{font-size:25px;font-weight:400;color:var(--muted);margin-bottom:12px}
.signup{display:grid;grid-template-columns:minmax(0,1fr) minmax(0,1fr);gap:10px 14px;text-align:left;width:100%}
.signup input,.signup select{width:100%;min-width:0;height:36px;border:1px solid #b9b9b9;padding:0 8px;font-family:"Lato",sans-serif;font-size:12px;color:var(--ink);background:var(--white)}
.signup select{grid-column:1/3}
.signup button{grid-column:1/3;justify-self:center;width:146px;height:36px;margin-top:4px;background:var(--navy);color:var(--white);border:0;font-family:"Montserrat",sans-serif;font-weight:700;font-size:13px}

/* section titles */
.sec-title{width:1200px;text-align:center;font-family:"Montserrat",sans-serif;font-weight:700;font-size:31px;text-transform:uppercase;color:var(--ink)}
.divider{left:530px;width:140px;height:14px}
.light .sec-title{color:var(--white)}

.products{top:770px;height:460px;background:var(--paper)}
.photo{box-shadow:0 2px 6px rgba(0,0,0,.25)}
.caption{font-family:"Montserrat",sans-serif;font-weight:700;font-size:15px;text-transform:uppercase}

.model{top:1230px;height:489px;background:var(--white)}
.model-card{top:166px;width:224px}
.model-card .photo{height:171px;border-radius:6px}
.model-card h5{font-family:"Montserrat",sans-serif;font-size:14px;margin:20px 0 8px}
.model-card p{font-size:13.5px;color:var(--muted);line-height:1.4}
.model-card a{display:block;margin-top:6px;color:var(--blue);font-weight:700;font-size:13px;text-decoration:none}

.pricing{top:1719px;height:501px;background:linear-gradient(135deg,var(--blue) 0%,#2bb0ea 50%,var(--blue-dark) 100%)}
.plan{top:155px;width:317px;height:262px;background:#e4e4e4;border-radius:4px;text-align:center;overflow:hidden;box-shadow:0 2px 5px rgba(0,0,0,.2)}
.plan-head{background:var(--white);height:75px;padding-top:14px}
.plan-head h6{font-size:21px;font-weight:400}
.plan-head span{font-size:14px}
.plan .price{font-family:"Montserrat",sans-serif;font-weight:700;font-size:36px;margin-top:18px}
.plan .price small{font-size:12px;font-weight:400}
.plan p{font-size:13.5px;color:var(--muted);line-height:1.4;padding:6px 40px 0}
.plan .cta{display:inline-block;margin-top:14px;width:118px;height:34px;line-height:34px;color:var(--white);font-size:13px}
.cta-bronze{background:var(--orange)}
.cta-silver{background:var(--teal)}
.cta-gold{background:var(--green)}

.about{top:2220px;height:319px;background:var(--white)}
.about-copy{left:155px;top:152px;width:892px;text-align:center;font-size:13.5px;line-height:1.75;color:var(--muted)}
.about-copy p+p{margin-top:8px}

.contact{top:2539px;height:660px;background:var(--navy)}
.field{border:1px solid #6c7685;background:var(--field);color:#c9d0da;font-size:12px;padding:10px 12px;font-style:italic}
.send{left:98px;top:385px;width:98px;height:36px;background:var(--blue);color:var(--white);font-size:13px;text-align:center;line-height:36px;font-family:"Montserrat",sans-serif}
.contact-info{left:648px;color:var(--white);font-size:13.5px;line-height:1.45;display:flex;gap:14px}
.contact-info b{font-family:"Montserrat",sans-serif}
.heads{left:0;top:490px;width:1200px;height:125px;background:linear-gradient(180deg,var(--navy) 0%,var(--blue) 60%,var(--blue-dark) 100%)}
.copyright{top:626px;width:1200px;text-align:center;color:#c9d0da;font-size:12px;letter-spacing:1px}
</style>
</head>
<body>

<header class="topbar">
  <div class="brand abs"><span class="brand-mark"></span><span class="brand-name">Velmora</span></div>
  <div class="contact-chip chip-phone abs">
    <svg width="34" height="30" viewBox="0 0 34 30"><path d="M6 4c3-2 6 3 7 6 1 2-3 3-2 5 2 3 4 5 7 6 2 1 3-3 5-2 3 1 8 4 6 7-2 3-7 3-12 0S6 16 4 11C3 8 3 6 6 4z" fill="none" stroke="#fff" stroke-width="2.4"/></svg>
    <div><small>CALL US NOW!</small><strong>555-210-4477</strong></div>
  </div>
  <div class="contact-chip chip-mail abs">
    <svg width="34" height="28" viewBox="0 0 34 28"><rect x="3" y="5" width="28" height="19" fill="none" stroke="#fff" stroke-width="2.4"/><path d="M3 5l14 11 14-11" fill="none" stroke="#fff" stroke-width="2.4"/></svg>
    <div><small>MAIL US</small><strong>hello@velmora-mail.com</strong></div>
  </div>
</header>

<section class="hero" role="img" aria-label="City skyline photograph behind the main offer">
  <nav class="mainnav abs">
    <a href="#home">Home</a><a href="#products">Products</a><a href="#model">Unique Model</a><a href="#pricing">Pricing</a><a href="#about">About</a><a href="#contact">Contact Us</a>
  </nav>
  <h1 class="hero-title abs">List And Audience Building For Your Content Marketing Efforts</h1>
  <h2 class="hero-sub abs">We Offer 2 Tracks Form Which To Choose:</h2>

  <div class="track track-1 abs"><div class="track-inner">
    <h3>Track 1</h3>
    <p>Update, enhance or adppend your existing prospect datasbase.<br>Give us your ideal target title, company size and industry<br>We provide contact lists derived from real-time data for your target including emails and phone numbers<br>Coming soon: Discover what services and technologies are being evaluated or used within your lists</p>
  </div></div>
  <div class="track-pointer abs" style="left:410px"></div>

  <div class="track track-2 abs"><div class="track-inner">
    <h3>Track 2</h3>
    <p>We use our data and email servers to send campaigns for you -<br>You get access to all the campaign results back and only pay for actions: openers and clickers</p>
  </div></div>
  <div class="track-pointer abs" style="left:781px"></div>

  <div class="track track-form abs"><div class="track-inner">
    <h3>Tell Us</h3>
    <h4>What You Want</h4>
    <form class="signup">
      <input type="text" placeholder="First Name">
      <input type="text" placeholder="Last Name">
      <input type="text" placeholder="Company">
      <input type="text" placeholder="Email Address">
      <select><option>Track 1</option><option>Track 2</option><option>Custom Combination</option></select>
      <button type="button">SUBMIT</button>
    </form>
  </div></div>
</section>

<section class="products" id="products">
  <h2 class="sec-title abs" style="top:28px">Products</h2>
  <svg class="divider abs" style="top:78px" viewBox="0 0 140 14"><line x1="0" y1="9" x2="58" y2="9" stroke="#999"/><rect x="63" y="3" width="14" height="9" fill="#888"/><line x1="82" y1="9" x2="140" y2="9" stroke="#999"/></svg>
  <div class="photo abs" style="left:150px;top:129px;width:433px;height:244px;background:linear-gradient(135deg,#dfe6ee,#7f93a8 60%,#2c3c52)" role="img" aria-label="Photograph of a business handshake"></div>
  <div class="photo abs" style="left:631px;top:129px;width:426px;height:244px;background:linear-gradient(135deg,#3a3630,#8a7a66 50%,#d8d2c8)" role="img" aria-label="Photograph of hands typing on a laptop"></div>
  <div class="caption abs" style="left:150px;top:384px">Products 1</div>
  <div class="caption abs" style="left:631px;top:384px">Product 2</div>
</section>

<section class="model" id="model">
  <h2 class="sec-title abs" style="top:60px">Unique Model</h2>
  <svg class="divider abs" style="top:110px" viewBox="0 0 140 14"><line x1="0" y1="9" x2="58" y2="9" stroke="#999"/><rect x="63" y="3" width="14" height="9" fill="#888"/><line x1="82" y1="9" x2="140" y2="9" stroke="#999"/></svg>
  <div class="model-card abs" style="left:98px">
    <div class="photo" style="background:linear-gradient(135deg,#1d3a5c,#4a88b8 55%,#c8d4de)" role="img" aria-label="Photograph of hands on a keyboard with data graphics"></div>
    <h5>MODEL 1</h5><p>Lorem Ipsum is simply dummy text of the printing and...</p><a href="#model">More ›</a>
  </div>
  <div class="model-card abs" style="left:357px">
    <div class="photo" style="background:linear-gradient(135deg,#0f2246,#2f5a9c 55%,#7aa0d0)" role="img" aria-label="Photograph of strategy gears with a pointing hand"></div>
    <h5>MODEL 2</h5><p>Contrary to popular belief, Lorem Ipsum is not simply random text...</p><a href="#model">More ›</a>
  </div>
  <div class="model-card abs" style="left:617px">
    <div class="photo" style="background:linear-gradient(135deg,#0c1f33,#2b5d86 55%,#5b8fb6)" role="img" aria-label="Photograph of a tablet in a server room"></div>
    <h5>MODEL 3</h5><p>Lorem Ipsum is simply dummy text of the printing ...</p><a href="#model">More ›</a>
  </div>
  <div class="model-card abs" style="left:877px">
    <div class="photo" style="background:linear-gradient(135deg,#f2f2f2,#cfcfcf 60%,#9a9a9a)" role="img" aria-label="Photograph of a sketched business idea board"></div>
    <h5>MODEL 4</h5><p>There are many variations of passages of Lorem...</p><a href="#model">More ›</a>
  </div>
</section>

<section class="pricing light" id="pricing">
  <h2 class="sec-title abs" style="top:50px">Pricing</h2>
  <svg class="divider abs" style="top:100px" viewBox="0 0 140 14"><line x1="0" y1="9" x2="58" y2="9" stroke="#fff"/><rect x="63" y="3" width="14" height="9" fill="#fff"/><line x1="82" y1="9" x2="140" y2="9" stroke="#fff"/></svg>
  <div class="plan abs" style="left:98px">
    <div class="plan-head"><h6>Bronze</h6><span>Package</span></div>
    <div class="price">$ 199 <small>/ Month</small></div>
    <p>Lorem Ipsum is simply dummy text of the printing and typesetting industry.</p>
    <span class="cta cta-bronze">Get it now</span>
  </div>
  <div class="plan abs" style="left:439px">
    <div class="plan-head"><h6>Silver</h6><span>Package</span></div>
    <div class="price">$ 339 <small>/ Month</small></div>
    <p>Lorem Ipsum is simply dummy text of the printing and typesetting industry.</p>
    <span class="cta cta-silver">Get it now</span>
  </div>
  <div class="plan abs" style="left:781px">
    <div class="plan-head"><h6>Gold</h6><span>Package</span></div>
    <div class="price">$ 689 <small>/ Month</small></div>
    <p>Lorem Ipsum is simply dummy text of the printing and typesetting industry.</p>
    <span class="cta cta-gold">Get it now</span>
  </div>
</section>

<section class="about" id="about">
  <h2 class="sec-title abs" style="top:42px">About Velmora</h2>
  <svg class="divider abs" style="top:92px" viewBox="0 0 140 14"><line x1="0" y1="9" x2="58" y2="9" stroke="#999"/><rect x="63" y="3" width="14" height="9" fill="#888"/><line x1="82" y1="9" x2="140" y2="9" stroke="#999"/></svg>
  <div class="about-copy abs">
    <p>Contrary to popular belief, Lorem Ipsum is not simply random text. It has roots in a piece of classical Latin literature from 45 BC, making it over 2000 years old. A Latin professor at a small college in Virginia looked up one of the more obscure Latin words, consectetur, from a Lorem Ipsum passage, and going through the cites of the word in classical literature, discovered the undoubtable source.</p>
    <p>Lorem Ipsum is simply dummy text of the printing and typesetting industry. Lorem Ipsum has been the industry's standard dummy text ever since the 1500s, when an unknown printer took a galley of type and scrambled it to make a type specimen book.</p>
  </div>
</section>

<section class="contact light" id="contact">
  <h2 class="sec-title abs" style="top:46px">Contact Us</h2>
  <svg class="divider abs" style="top:96px" viewBox="0 0 140 14"><line x1="0" y1="9" x2="58" y2="9" stroke="#fff"/><rect x="63" y="3" width="14" height="9" fill="#fff"/><line x1="82" y1="9" x2="140" y2="9" stroke="#fff"/></svg>
  <div class="field abs" style="left:98px;top:152px;width:244px;height:39px">Name</div>
  <div class="field abs" style="left:357px;top:152px;width:242px;height:39px">Phone No.</div>
  <div class="field abs" style="left:98px;top:214px;width:501px;height:38px">Email</div>
  <div class="field abs" style="left:98px;top:264px;width:501px;height:100px">Message</div>
  <div class="send abs">SUBMIT</div>
  <div class="abs" style="left:644px;top:141px;width:463px;height:200px;background:linear-gradient(135deg,#e8e4da,#d6dccf 50%,#c9d6e2)" role="img" aria-label="Map showing the office location"></div>
  <div class="contact-info abs" style="top:366px">
    <svg width="16" height="22" viewBox="0 0 16 22"><path d="M8 1a7 7 0 0 0-7 7c0 5 7 13 7 13s7-8 7-13a7 7 0 0 0-7-7z" fill="#fff"/><circle cx="8" cy="8" r="2.6" fill="#1b2330"/></svg>
    <div><b>VELMORA</b><br>123, Lorem Ipsum Dolor Sit Amet, Consectetur</div>
  </div>
  <div class="contact-info abs" style="top:412px">
    <svg width="18" height="18" viewBox="0 0 18 18"><path d="M3 2c2-1 3 2 4 3 0 1-2 2-1 3 1 2 2 3 4 4 1 0 2-2 3-1 2 1 4 2 3 4-1 2-4 2-7 0S4 9 2 6C1 4 1 3 3 2z" fill="#fff"/></svg>
    <div>Call Us: 555-210-4477<br>Email Us: hello@velmora-mail.com</div>
  </div>
  <div class="heads abs" role="img" aria-label="Row of blue silhouette heads illustration"></div>
  <div class="copyright abs">© 2016 &nbsp;VELMORA ALL RIGHTS RESERVED.</div>
</section>

</body>
</html>
```